Book Cover Design

Design with title UNWAVERING
Subtitle: Ways to Kindle the Spark of Resolve
Author Name: Carla Jean Morrow
Put DAILY MERIDIAN BESTSELLER at top
Shimmer design, see inspirational images attached

```html
<!DOCTYPE html>
<html lang="en">
<head>
<meta charset="utf-8">
<title>Unwavering — Book Cover</title>
<link rel="stylesheet" href="https://fonts.googleapis.com/css2?family=Bebas+Neue&display=swap">
<style>
  :root {
    --bg: #e4e4e4;
    --ink: #141414;
    --cyan: #7fe6e6;
    --aqua: #a6f0dc;
    --pink: #f2a6d6;
    --peach: #f7c9a4;
    --lilac: #b9a6ee;
    --butter: #f3ecb0;
  }
  * { margin: 0; padding: 0; box-sizing: border-box; }
  html, body { width: 1200px; height: 2400px; overflow: hidden; }
  body {
    background: var(--bg);
    font-family: "Bebas Neue", "Oswald", sans-serif;
    color: var(--ink);
    position: relative;
  }
  h1, h2, h3, p { font-weight: 400; }
  .shimmer {
    background:
      radial-gradient(ellipse 30% 40% at 15% 20%, var(--pink), transparent 70%),
      radial-gradient(ellipse 35% 30% at 70% 15%, var(--lilac), transparent 70%),
      radial-gradient(ellipse 30% 35% at 45% 60%, var(--peach), transparent 70%),
      radial-gradient(ellipse 40% 30% at 85% 75%, var(--pink), transparent 70%),
      radial-gradient(ellipse 30% 30% at 25% 85%, var(--butter), transparent 70%),
      radial-gradient(ellipse 35% 40% at 60% 35%, var(--aqua), transparent 70%),
      linear-gradient(135deg, var(--cyan), var(--lilac) 45%, var(--aqua) 75%, var(--peach));
  }

  /* Full jacket: back + spine + front */
  .jacket {
    position: absolute;
    left: 40px; top: 80px;
    width: 1120px; height: 640px;
    display: flex;
  }
  .back-cover { position: relative; width: 530px; height: 100%; }
  .synopsis-title {
    position: absolute; left: 45px; top: 200px;
    font-size: 32px; line-height: 1; letter-spacing: 0.02em;
  }
  .synopsis-text {
    position: absolute; left: 45px; top: 242px; width: 440px;
    font-size: 15px; line-height: 1.3; letter-spacing: 0.04em;
  }
  .spine {
    position: relative; width: 50px; height: 100%;
    display: flex; flex-direction: column; align-items: center;
    padding: 25px 0;
    gap: 40px;
  }
  .spine span { writing-mode: vertical-rl; white-space: nowrap; line-height: 1; }
  .spine-title { font-size: 46px; }
  .spine-author { font-size: 22px; letter-spacing: 0.05em; }

  /* Front cover component, laid out in cover units (--u) */
  .front-cover {
    --u: 10px;
    position: relative;
    width: calc(var(--u) * 54);
    height: calc(var(--u) * 64);
  }
  .cover-label {
    position: absolute; top: calc(var(--u) * 3); left: 0; right: 0;
    text-align: center; font-size: calc(var(--u) * 2.4); line-height: 1;
    letter-spacing: 0.02em;
  }
  .cover-title {
    position: absolute; top: calc(var(--u) * 6); left: 0; right: 0;
    text-align: center; font-size: calc(var(--u) * 10.5); line-height: 1;
  }
  .cover-subtitle {
    position: absolute; left: calc(var(--u) * 6); top: calc(var(--u) * 20);
    font-size: calc(var(--u) * 6); line-height: 1.05;
  }
  .cover-author {
    position: absolute; bottom: calc(var(--u) * 6); left: 0; right: 0;
    text-align: center; font-size: calc(var(--u) * 2.5); line-height: 1;
    letter-spacing: 0.04em;
  }

  .standalone {
    --u: 11.85px;
    position: absolute;
    left: 280px; top: 860px;
    box-shadow: 0 12px 30px rgba(0,0,0,0.12);
  }
</style>
</head>
<body>

<section class="jacket shimmer" role="img" aria-label="Holographic shimmer pattern in cyan, pink, peach and lilac across the full book jacket">
  <div class="back-cover">
    <h3 class="synopsis-title">Synopsis</h3>
    <p class="synopsis-text">When doubt grows loud, resolve grows quiet. This book shows how steady belief is built one small choice at a time. Through honest stories and simple daily practices, you will learn to trust your own voice, hold firm under pressure, and turn hesitation into action. Kindle the spark, protect it, and let it carry you forward.</p>
  </div>
  <div class="spine">
    <span class="spine-title">Unwavering</span>
    <span class="spine-author">By Carla Jean Morrow</span>
  </div>
  <div class="front-cover">
    <p class="cover-label">Daily Meridian Best Seller</p>
    <h1 class="cover-title">Unwavering</h1>
    <h2 class="cover-subtitle">Ways to<br>Kindle the<br>Spark of<br>Resolve</h2>
    <p class="cover-author">By Carla Jean Morrow</p>
  </div>
</section>

<section class="front-cover standalone shimmer" role="img" aria-label="Front cover with holographic shimmer pattern in cyan, pink, peach and lilac">
  <p class="cover-label">Daily Meridian Best Seller</p>
  <h1 class="cover-title">Unwavering</h1>
  <h2 class="cover-subtitle">Ways to<br>Kindle the<br>Spark of<br>Resolve</h2>
  <p class="cover-author">By Carla Jean Morrow</p>
</section>

</body>
</html>
```